Truck Drivers Using App w/Jobsite Checklist

Looking for an 8" x 11" flyer that conveys to our customers (roofing contractors) that our drivers have tablets in each truck that have an app with a jobsite checklist that gives contractors less real time notifications and mistakes are caught with photos.
Should read something like this:
Ever wonder if your material has been delivered? We've got a solution for that!
All Trucks are equipped with dash-mounted tablet.
Here's what you get access to:
- Real Time Email Confirmation of Delivery
- Photos of Material Placement
- Before/After Photo of Driveway
- Material List of Products Delivered
- Homeowner Sign Off
Maybe a collage of the different photos available.
Target Market(s)
Roofing/Building Contractors
Industry/Entity Type
Roofing
Requirements
Must have
- website: www.harborfinchdepot.com
- tagline: Building Relationships, Building Trust - a Tradition Since 1905
- Photoshop format for further editing
Nice to have
- A smooth look to it.
- A collage of the photos avail on app

```html
<!DOCTYPE html>
<html lang="en">
<head>
<meta charset="utf-8">
<title>Harbor Finch Depot – Delivery Tablet Flyer</title>
<link rel="stylesheet" href="https://fonts.googleapis.com/css2?family=Roboto+Condensed:wght@700&family=Open+Sans:wght@400;600;700&display=swap">
<style>
  :root{
    --brand-blue:#1b5aa5;
    --brand-blue-dark:#0f3f7c;
    --ink:#1f2630;
    --paper:#eceeef;
    --stage:#d9dbdd;
    --white:#ffffff;
  }
  html,body{margin:0;padding:0;width:1020px;height:1200px;overflow:hidden;background:var(--stage);}
  .flyer{
    position:absolute;left:78px;top:6px;width:864px;height:1187px;
    background:var(--paper);overflow:hidden;
    font-family:"Open Sans",Arial,sans-serif;color:var(--ink);
  }
  .flyer-art{position:absolute;left:0;top:0;width:864px;height:1187px;}
  .tagline{position:absolute;left:0;width:864px;text-align:center;margin:0;
    font-family:"Roboto Condensed","Arial Narrow",sans-serif;font-weight:700;line-height:1;}
  .tagline-main{top:36px;font-size:62px;color:var(--brand-blue);letter-spacing:.5px;}
  .tagline-sub{top:100px;font-size:40px;color:var(--brand-blue);}
  .tagline-since{top:146px;font-size:36px;color:var(--ink);}
  .pitch{position:absolute;left:0;width:906px;text-align:center;margin:0;color:var(--brand-blue);}
  .pitch-question{top:788px;font-size:26px;font-weight:700;}
  .pitch-answer{top:822px;font-size:28px;}
  .pitch-note{top:860px;font-size:16px;}
  .access-heading{position:absolute;left:0;top:916px;width:292px;height:35px;padding-left:22px;
    background:var(--brand-blue);border-radius:0 18px 18px 0;color:var(--white);
    font-size:19px;font-weight:700;line-height:35px;}
  .access-list{position:absolute;left:22px;top:970px;margin:0;padding:0;list-style:none;}
  .access-list li{display:flex;align-items:center;height:21.5px;font-size:13.5px;color:var(--ink);}
  .access-list svg{width:12px;height:12px;margin-right:12px;}
  .brand-name{position:absolute;left:330px;top:1010px;width:250px;display:flex;align-items:center;gap:10px;
    font-size:22px;font-weight:700;color:var(--brand-blue);white-space:nowrap;}
  .brand-dot{width:20px;height:20px;border-radius:50%;background:var(--brand-blue);flex:none;}
  .web-bar{position:absolute;left:0;top:1095px;width:864px;height:92px;
    background:linear-gradient(90deg,var(--brand-blue-dark) 0%,var(--brand-blue) 55%,#6f9fd4 85%,#dfe8f2 100%);}
  .web-address{position:absolute;left:30px;top:1126px;display:flex;align-items:center;gap:14px;
    color:var(--white);font-size:22px;}
  .web-address svg{width:26px;height:26px;}
  .rep-photo{position:absolute;left:645px;top:855px;width:219px;height:332px;
    background:linear-gradient(180deg,#c9b49c 0%,#d8e04a 45%,#6f8fb5 80%,#3c4a5a 100%);
    border-radius:90px 90px 0 0;}
</style>
</head>
<body>
<main class="flyer">
  <svg class="flyer-art" viewBox="0 0 576 791" aria-hidden="false">
    <defs>
      <clipPath id="collage-window">
        <path d="M0,172 Q288,118 576,172 L576,438 Q288,535 0,438 Z"/>
      </clipPath>
      <linearGradient id="sky-truck" x1="0" y1="0" x2="0" y2="1">
        <stop offset="0" stop-color="#6fa6de"/><stop offset=".5" stop-color="#e8eef3"/><stop offset="1" stop-color="#55595c"/>
      </linearGradient>
      <linearGradient id="dash-tablet" x1="0" y1="0" x2="0" y2="1">
        <stop offset="0" stop-color="#c9ccce"/><stop offset=".45" stop-color="#8e9295"/><stop offset="1" stop-color="#2b2d30"/>
      </linearGradient>
      <linearGradient id="driveway" x1="0" y1="0" x2="1" y2="1">
        <stop offset="0" stop-color="#7d7f82"/><stop offset="1" stop-color="#a3a4a6"/>
      </linearGradient>
      <linearGradient id="pallets" x1="0" y1="0" x2="0" y2="1">
        <stop offset="0" stop-color="#5f6f52"/><stop offset=".5" stop-color="#9fb0bb"/><stop offset="1" stop-color="#c9c3b3"/>
      </linearGradient>
      <linearGradient id="bags" x1="0" y1="0" x2="0" y2="1">
        <stop offset="0" stop-color="#7fb3e3"/><stop offset=".45" stop-color="#e9e6e6"/><stop offset="1" stop-color="#b94a4a"/>
      </linearGradient>
    </defs>

    <path class="collage-frame" d="M0,160 Q288,102 576,160 L576,456 Q288,560 0,456 Z" fill="#1b5aa5"/>
    <path d="M0,166 Q288,110 576,166 L576,170 Q288,116 0,170 Z" fill="#eceeef" opacity=".9"/>

    <g clip-path="url(#collage-window)">
      <rect x="0" y="100" width="576" height="460" fill="#eceeef"/>
      <g role="img" aria-label="Photo: flatbed delivery truck with crane loaded with roofing material">
        <rect x="0" y="150" width="162" height="175" fill="url(#sky-truck)"/>
      </g>
      <g role="img" aria-label="Photo: pallets of roofing shingles stacked on a driveway">
        <rect x="0" y="329" width="162" height="200" fill="url(#pallets)"/>
      </g>
      <g role="img" aria-label="Photo: dash-mounted tablet showing the delivery checklist app">
        <rect x="166" y="100" width="244" height="460" fill="url(#dash-tablet)"/>
      </g>
      <g role="img" aria-label="Photo: concrete driveway before delivery">
        <rect x="414" y="150" width="162" height="175" fill="url(#driveway)"/>
      </g>
      <g role="img" aria-label="Photo: wrapped bundles of roofing material on a truck bed">
        <rect x="414" y="329" width="162" height="200" fill="url(#bags)"/>
      </g>
    </g>
    <path d="M0,438 Q288,535 576,438 L576,444 Q288,541 0,444 Z" fill="#ffffff" opacity=".55"/>
  </svg>

  <h1 class="tagline tagline-main">BUILDING RELATIONSHIPS</h1>
  <p class="tagline tagline-sub">BUILDING TRUST</p>
  <p class="tagline tagline-since">A TRADITION SINCE 1905</p>

  <p class="pitch pitch-question">Ever wonder if your material has been delivered?</p>
  <p class="pitch pitch-answer">We've got a solution for that!</p>
  <p class="pitch pitch-note">All Trucks are equipped with dash-mounted tablet.</p>

  <div class="access-heading">Here's what you get access to:</div>
  <ul class="access-list">
    <li><svg viewBox="0 0 12 12"><path d="M1.5,6.5 L4.5,9.5 L10.5,2.5" fill="none" stroke="#1b5aa5" stroke-width="1.8"/></svg>Real Time Email Confirmation of Delivery</li>
    <li><svg viewBox="0 0 12 12"><path d="M1.5,6.5 L4.5,9.5 L10.5,2.5" fill="none" stroke="#1b5aa5" stroke-width="1.8"/></svg>Photos of Material Placement</li>
    <li><svg viewBox="0 0 12 12"><path d="M1.5,6.5 L4.5,9.5 L10.5,2.5" fill="none" stroke="#1b5aa5" stroke-width="1.8"/></svg>Before/After Photo of Driveway</li>
    <li><svg viewBox="0 0 12 12"><path d="M1.5,6.5 L4.5,9.5 L10.5,2.5" fill="none" stroke="#1b5aa5" stroke-width="1.8"/></svg>Material List of Products Delivered</li>
    <li><svg viewBox="0 0 12 12"><path d="M1.5,6.5 L4.5,9.5 L10.5,2.5" fill="none" stroke="#1b5aa5" stroke-width="1.8"/></svg>Homeowner Sign Off</li>
  </ul>

  <div class="brand-name"><span class="brand-dot"></span>Harbor Finch Depot</div>

  <div class="web-bar"></div>
  <div class="web-address">
    <svg viewBox="0 0 26 26"><g fill="none" stroke="#ffffff" stroke-width="1.6"><circle cx="13" cy="13" r="11"/><ellipse cx="13" cy="13" rx="5" ry="11"/><line x1="2" y1="13" x2="24" y2="13"/><path d="M4,7.5 H22 M4,18.5 H22"/></g></svg>
    <span>www.harborfinchdepot.com</span>
  </div>

  <div class="rep-photo" role="img" aria-label="Photo: smiling delivery representative in a high-visibility vest holding a tablet"></div>
</main>
</body>
</html>
```